Plakat-Design 24h Betreuung
Zielgruppe
Wir vermitteln 24h Pflege- und Betreuungskräfte für alte und hilfbedürftige Menschen!
Zielgruppe: deren Angehörige (zwischen 50-70 Jahre alt)
Aufgabenstellung
Klare Ansage - nicht zu verspielt - geradlinig
Maße Plakat: 504 cm breit x 238 cm hoch
Das PLAKAT ist ca 10 m von der Straße entfernet und ist für Autofahrer gedacht - somit muss man alles gut lesen können und groß geschrieben sein !!!!
Folgender Text und Bilder sollte das Plakat beinhalten:
24h - Betreuung (groß links oben platziert)
Logo: SorgeHafen.at
Foto mit 10 Personen
Erfahrung seit 2010
www.sorgehafen.at

```html
<!DOCTYPE html>
<html lang="de">
<head>
<meta charset="utf-8">
<title>24h - Betreuung Plakat</title>
<link href="https://fonts.googleapis.com/css2?family=Montserrat:wght@500;700;800&display=swap" rel="stylesheet">
<style>
  :root {
    --backdrop: #dededd;
    --paper: #ffffff;
    --navy: #2b4380;
    --orange: #dc6a20;
    --photo-light: #eef0f4;
    --photo-dark: #8a97b3;
  }
  * { margin: 0; padding: 0; box-sizing: border-box; }
  html, body { width: 1023px; height: 1200px; overflow: hidden; }
  body { background: var(--backdrop); font-family: "Montserrat", sans-serif; position: relative; }
  .poster {
    position: absolute; left: 61px; width: 902px; height: 479px;
    background: var(--paper); overflow: hidden;
  }
  .poster--banded { top: 60px; }
  .poster--plain { top: 660px; }
  .headline {
    position: absolute; left: 173px; top: 24px;
    font-weight: 800; font-size: 66px; letter-spacing: -0.3px; color: var(--navy);
    line-height: 1; white-space: nowrap;
  }
  .team-photo {
    position: absolute; left: 237px; top: 117px; width: 458px; height: 336px;
    background: radial-gradient(ellipse at 50% 45%, var(--photo-dark) 0%, #b7c0d3 45%, var(--photo-light) 80%, transparent 100%);
    border-radius: 40% 40% 30% 30%;
  }
  .experience-badge { position: absolute; left: 0; top: 0; width: 902px; height: 479px; }
  .experience-text {
    position: absolute; left: 18px; top: 356px; width: 184px; text-align: center;
    color: var(--paper); font-weight: 500; font-size: 32px; line-height: 34px;
  }
  .brand {
    position: absolute; left: 595px; top: 356px; width: 250px; height: 90px;
  }
  .brand-dot {
    position: absolute; right: 0; top: 0; width: 44px; height: 44px;
    border-radius: 50%; background: var(--orange);
  }
  .brand-name {
    position: absolute; right: 0; bottom: 0;
    font-weight: 700; font-size: 31px; color: var(--navy); line-height: 1; white-space: nowrap;
  }
  .base-band {
    position: absolute; left: 0; bottom: 0; width: 100%; height: 12px; background: var(--navy);
  }
</style>
</head>
<body>
  <section class="poster poster--banded">
    <h1 class="headline">24h - Betreuung</h1>
    <div class="team-photo" role="img" aria-label="Gruppenfoto des Teams mit zehn Personen in weißen Blusen und Jeans"></div>
    <div class="base-band"></div>
    <svg class="experience-badge" viewBox="0 0 902 479" aria-hidden="true">
      <circle cx="100" cy="409" r="130" fill="var(--orange)"/>
      <circle cx="100" cy="409" r="120" fill="var(--navy)"/>
    </svg>
    <p class="experience-text">Erfahrung<br>seit 2010</p>
    <div class="brand">
      <span class="brand-dot"></span>
      <p class="brand-name">SorgeHafen.at</p>
    </div>
  </section>

  <section class="poster poster--plain">
    <h1 class="headline">24h - Betreuung</h1>
    <div class="team-photo" role="img" aria-label="Gruppenfoto des Teams mit zehn Personen in weißen Blusen und Jeans"></div>
    <svg class="experience-badge" viewBox="0 0 902 479" aria-hidden="true">
      <circle cx="100" cy="409" r="130" fill="var(--orange)"/>
      <circle cx="100" cy="409" r="120" fill="var(--navy)"/>
    </svg>
    <p class="experience-text">Erfahrung<br>seit 2010</p>
    <div class="brand">
      <span class="brand-dot"></span>
      <p class="brand-name">SorgeHafen.at</p>
    </div>
  </section>
</body>
</html>
```